Bright Harbour Tutors Facebook business page

I currently have a website with a CSS template www.brightharbourtutors.co.uk. I am now seeking to have graphics designed in a complimentary style for:

1. A Facebook business landing page
Updates

Dear all,

Thank you to those of you that have submitted designs so far.  Please note that the brief and title of this project has changed.  I now simply require a Facebook business page designing and not a Twitter and Youtube page also.

I hope that you will all find the budget more attractive now.

Regards

Gareth

Dear all,  your submissions sor far have been very creative.  As further guidance, I would like to see an innovative and creative adaptation and/or embellishment of my 'digital man'.  He could in some way be indicating a call to action to 'like' my page.

The use also of an additional key message: The future of marketing is digital 

This could be integral to a design theme.

I hope that this helps.

Thank you all

Gareth

Target Market(s)

Small and medium sized businesses, students 18-25, Apprentices, marketing professionals

Industry/Entity Type

Business

Requirements
Must have
• Ideally, my logo must appear each page with my slogan 'let us teach you how'. The font used is Arial Rounded MT. For the Facebook landing page, I would like the call to action to be 'getting people to like my page'. Therefore a innovative way of pointing to the like button (see http://www.plumvex.example/zestorafizz). Maybe this could be an adaptation of my icon, the digital man. It needs to be innovative and eyecatching whilst maintaing my corporate colours. I teach courses in Social Media so I need to have impressive pages! I also am keen to see what creative ideas you can come up with!

```html
<!DOCTYPE html>
<html lang="en">
<head>
<meta charset="utf-8">
<title>Bright Harbour Tutors – Facebook Page</title>
<link href="https://fonts.googleapis.com/css2?family=Nunito:wght@700;800&display=swap" rel="stylesheet">
<style>
  :root {
    --paper: #ffffff;
    --frame: #f6e3a0;
    --sun: #f9b20f;
    --sun-soft: #fdd55a;
    --sun-pale: #fff3cc;
    --badge: #ec5a2c;
    --badge-edge: #f58a5c;
    --ink: #3a3a3a;
    --ink-soft: #6b6b6b;
    --accent: #f7a600;
  }
  html, body {
    margin: 0;
    padding: 0;
    overflow: hidden;
    background: var(--paper);
  }
  .page {
    position: relative;
    width: 903px;
    height: 1200px;
    box-sizing: border-box;
    border: 2px solid var(--frame);
    overflow: hidden;
    background: var(--paper);
    font-family: "Nunito", "Arial Rounded MT Bold", sans-serif;
  }
  .backdrop {
    position: absolute;
    inset: 0;
  }
  .like-badge {
    position: absolute;
    left: 660px;
    top: 24px;
    width: 210px;
    height: 210px;
  }
  .brand {
    position: absolute;
    left: 0;
    right: 0;
    top: 150px;
    text-align: center;
  }
  .brand-dot {
    display: block;
    width: 120px;
    height: 120px;
    margin: 0 auto 50px;
    border-radius: 50%;
    background: var(--sun);
  }
  .brand-name {
    margin: 0;
    font-size: 52px;
    font-weight: 800;
    color: var(--ink);
    letter-spacing: -0.5px;
  }
  .slogan {
    position: absolute;
    left: 0;
    right: 0;
    top: 555px;
    margin: 0;
    text-align: center;
    font-size: 58px;
    font-weight: 800;
    color: var(--ink);
    letter-spacing: -0.5px;
  }
  .services {
    position: absolute;
    left: 78px;
    top: 648px;
    width: 712px;
    height: 44px;
    margin: 0;
    padding: 0;
    list-style: none;
    display: flex;
    justify-content: center;
    align-items: center;
    gap: 18px;
    border-radius: 22px;
    background: var(--accent);
    font-size: 22px;
    font-weight: 700;
    color: var(--ink);
  }
  .services li + li::before {
    content: "•";
    margin-right: 18px;
  }
  .contact {
    position: absolute;
    right: 34px;
    bottom: 18px;
    margin: 0;
    display: flex;
    align-items: baseline;
    gap: 14px;
  }
  .contact-label {
    font-size: 34px;
    font-weight: 800;
    color: var(--ink-soft);
  }
  .contact-phone {
    font-size: 42px;
    font-weight: 800;
    color: var(--accent);
  }
</style>
</head>
<body>
<main class="page">
  <svg class="backdrop" width="903" height="1200" viewBox="0 0 903 1200" aria-hidden="true">
    <defs>
      <radialGradient id="glow" cx="0.35" cy="0.72" r="0.75">
        <stop offset="0" stop-color="#fbbd24"/>
        <stop offset="0.45" stop-color="#fde08a"/>
        <stop offset="1" stop-color="#ffffff"/>
      </radialGradient>
      <linearGradient id="swoosh" x1="0" y1="0" x2="1" y2="0">
        <stop offset="0" stop-color="#ffffff" stop-opacity="0.9"/>
        <stop offset="0.6" stop-color="#ffffff" stop-opacity="0.35"/>
        <stop offset="1" stop-color="#ffffff" stop-opacity="0"/>
      </linearGradient>
      <linearGradient id="band" x1="0" y1="0" x2="1" y2="0">
        <stop offset="0" stop-color="#f9a800" stop-opacity="0.7"/>
        <stop offset="1" stop-color="#fcd04a" stop-opacity="0.2"/>
      </linearGradient>
    </defs>
    <rect width="903" height="1200" fill="url(#glow)"/>
    <path d="M0 820 C220 760 480 700 903 900 L903 980 C520 800 260 820 0 900 Z" fill="url(#swoosh)"/>
    <path d="M0 980 C260 900 560 880 903 1010 L903 1080 C560 950 300 960 0 1060 Z" fill="url(#band)"/>
    <path d="M0 1060 C300 980 600 1000 903 1120 L903 1200 L0 1200 Z" fill="#fde7a4" opacity="0.6"/>
  </svg>

  <svg class="like-badge" viewBox="0 0 210 210" role="img" aria-label="Like our page">
    <defs>
      <path id="badge-arc" d="M40 105 A65 65 0 0 1 170 105"/>
    </defs>
    <g transform="rotate(40 105 105)">
      <circle cx="105" cy="105" r="100" fill="var(--badge-edge)"/>
      <circle cx="105" cy="105" r="90" fill="var(--badge)"/>
      <circle cx="105" cy="105" r="48" fill="#ffffff"/>
      <text font-family="Nunito, sans-serif" font-weight="800" font-size="22" fill="#ffffff" letter-spacing="4">
        <textPath href="#badge-arc" startOffset="50%" text-anchor="middle">LIKE OUR PAGE</textPath>
      </text>
    </g>
  </svg>

  <header class="brand">
    <span class="brand-dot" aria-hidden="true"></span>
    <h1 class="brand-name">Bright Harbour Tutors</h1>
  </header>

  <p class="slogan">Let us teach you how</p>

  <ul class="services">
    <li>Social Media</li>
    <li>Mobile Marketing</li>
    <li>Web Analytics</li>
  </ul>

  <p class="contact">
    <span class="contact-label">Get in touch</span>
    <span class="contact-phone">0845 270 318</span>
  </p>
</main>
</body>
</html>
```